Journal to help kids Grades 1-5 be more creative thinkers

This is a journal for kids grades 1 - 5 where they can write, color, draw and be creative. It is designed to accompany our children's book and after-school program called Pebble Pathfinders Club. We want children to use their imagination and sense of wonder as they color, create new ideas, write stories and learn all about the creative problems solving method. We want them to learn about how to use their feelings and help others in their community. We have based this on our ORBIT method, which helps teachers teach their curriculum by engaging kids in relevant and meaningful ways and helping children of all ages learn how to think for themselves. We are a non-profit organization, so all the sales go to a scholarship fund that helps teachers pay for coaching and professional development. This journal may be used in after school programs, at home, or in classrooms. We wanted the inside to be black and white so kids feel free to make it their own but the cover should be bright and inviting. This is written and designed by Molly Drabek and Rosa Penhallow on behalf of Lantern 3 ORBIT.

Target Market(s)

Parents, schools, after school programs

Industry/Entity Type

Education

Other font styles liked:
• Fun for kids

Requirements
Must have
• Bright fun colors, our logo, easy to read font for kids
Nice to have
• Our 6 characters - but we do have them throughout book -

```html
<!DOCTYPE html>
<html lang="en">
<head>
<meta charset="utf-8">
<title>Pebble Pathfinders Journal — Cover</title>
<link rel="stylesheet" href="https://fonts.googleapis.com/css2?family=Fredoka:wght@500;600&family=Inter:wght@400;700&display=swap">
<style>
  :root {
    --backdrop: #282828;
    --paper: #ffffff;
    --teal: #1297aa;
    --orange: #f28522;
    --green: #6a9f3d;
    --ink: #111111;
  }
  * { margin: 0; padding: 0; box-sizing: border-box; }
  html, body {
    width: 1200px; height: 1200px; overflow: hidden;
    background: var(--backdrop);
  }
  .cover {
    position: absolute; left: 170px; top: 42px;
    width: 861px; height: 1115px;
    background: var(--paper);
    overflow: hidden;
  }
  .art {
    position: absolute; inset: 0;
  }
  .art-top {
    background:
      radial-gradient(ellipse 170px 110px at 400px 80px, rgba(94,116,130,.55), transparent 75%),
      radial-gradient(ellipse 140px 120px at 700px 130px, rgba(185,227,236,.9), transparent 75%),
      radial-gradient(ellipse 110px 150px at 60px 110px, rgba(157,194,60,.8), transparent 75%),
      radial-gradient(ellipse 90px 60px at 810px 40px, rgba(227,34,106,.7), transparent 75%),
      radial-gradient(ellipse 60px 40px at 420px 170px, rgba(252,196,44,.7), transparent 75%);
  }
  .art-left {
    background:
      radial-gradient(ellipse 80px 70px at 50px 310px, rgba(94,116,130,.6), transparent 75%),
      radial-gradient(ellipse 90px 150px at 20px 470px, rgba(252,196,44,.8), transparent 75%),
      radial-gradient(ellipse 90px 90px at 100px 740px, rgba(200,205,210,.7), transparent 75%);
  }
  .art-right {
    background:
      radial-gradient(ellipse 110px 130px at 841px 250px, rgba(94,116,130,.45), transparent 75%),
      radial-gradient(ellipse 70px 110px at 851px 450px, rgba(106,159,61,.85), transparent 75%),
      radial-gradient(ellipse 70px 120px at 861px 610px, rgba(238,109,159,.55), transparent 75%),
      radial-gradient(ellipse 60px 80px at 851px 810px, rgba(94,116,130,.5), transparent 75%);
  }
  .art-bottom {
    background:
      radial-gradient(ellipse 120px 200px at 40px 1055px, rgba(18,151,170,.75), transparent 75%),
      radial-gradient(ellipse 180px 110px at 150px 975px, rgba(185,227,236,.8), transparent 75%),
      radial-gradient(ellipse 90px 120px at 310px 945px, rgba(94,116,130,.45), transparent 75%),
      radial-gradient(ellipse 150px 90px at 390px 1105px, rgba(252,196,44,.6), transparent 75%),
      radial-gradient(ellipse 130px 130px at 680px 945px, rgba(238,109,159,.55), transparent 75%),
      radial-gradient(ellipse 110px 180px at 830px 975px, rgba(238,109,159,.6), transparent 75%);
  }
  .title {
    position: absolute; left: 0; right: 0; top: 372px;
    text-align: center;
    font-family: "Fredoka", sans-serif;
    font-weight: 500;
    line-height: 1;
  }
  .title span { display: block; }
  .title-line-1 { color: var(--teal); font-size: 120px; }
  .title-line-2 { color: var(--orange); font-size: 114px; margin-top: 28px; letter-spacing: 1px; }
  .title-line-3 { color: var(--green); font-size: 114px; margin-top: 26px; }
  .club-mark {
    position: absolute; left: 0; right: 0; top: 922px;
    text-align: center;
    font-family: "Fredoka", sans-serif;
    font-weight: 600;
    font-size: 22px;
    color: var(--teal);
    line-height: 1.1;
  }
  .byline {
    position: absolute; left: 0; right: 0; top: 1030px;
    text-align: center;
    font-family: "Inter", sans-serif;
    font-size: 21px;
    color: var(--ink);
    letter-spacing: -0.3px;
  }
  .byline strong { font-weight: 700; }
</style>
</head>
<body>
  <main class="cover">
    <div class="art art-top" role="img" aria-label="Watercolour paint tray, brushes and pencils with colourful paint splashes"></div>
    <div class="art art-left" role="img" aria-label="Paint tube cap and yellow paint splatter"></div>
    <div class="art art-right" role="img" aria-label="Paintbrush, pencil, green paint splash and palette"></div>
    <div class="art art-bottom" role="img" aria-label="Colour pencils, brushes and blue, yellow and pink paint splashes"></div>

    <h1 class="title">
      <span class="title-line-1">Pebble</span>
      <span class="title-line-2">Pathfinders</span>
      <span class="title-line-3">Journal</span>
    </h1>

    <div class="club-mark">Pebble Pathfinders Club</div>

    <p class="byline"><strong>written and designed by</strong> Molly Drabek and Rosa Penhallow</p>
  </main>
</body>
</html>
```